Website visual upgrade

I am seeking expressions of interest for the updating the visuals of my website www.lunvaleplacements.example
I am basically seeking a simple,bold and visually strong graphic makeover.using existing or shortly to be modified text.

```html
<!DOCTYPE html>
<html lang="en">
<head>
<meta charset="utf-8">
<title>Lunvale Placements</title>
<link rel="stylesheet" href="https://fonts.googleapis.com/css2?family=Source+Sans+3:wght@400;600;700&family=Ubuntu:wght@400;500&display=swap">
<style>
:root{
  --red:#c8102e;
  --red-dark:#8f0a1f;
  --ink:#1a1a1a;
  --bar:#231f20;
  --grey:#e6e6e6;
  --mid:#8a8a8a;
  --white:#ffffff;
}
*{box-sizing:border-box;margin:0;padding:0}
html,body{width:1200px;height:917px;overflow:hidden;background:var(--white);font-family:"Source Sans 3",Arial,sans-serif;color:var(--ink)}
.wrap{position:absolute;left:250px;width:700px}

.topbar{position:absolute;top:0;left:0;width:1200px;height:38px;background:var(--bar)}
.audience{position:absolute;left:254px;top:13px;font:9px Arial,sans-serif;color:var(--white);letter-spacing:.3px}
.audience .active{text-decoration:underline}
.login{position:absolute;left:571px;top:8px;display:flex;gap:6px}
.login .field{width:130px;height:17px;border-radius:4px;background:var(--white);font:8px Arial,sans-serif;color:#aaa;padding:3px 8px}
.login .btn{height:17px;padding:0 8px;background:var(--red);border:1px solid #e86070;color:var(--white);font:8px Arial,sans-serif;line-height:15px}
.login-notes{position:absolute;top:28px;font:7px Arial,sans-serif;color:var(--white)}

.brand{position:absolute;left:250px;top:60px;display:flex;align-items:center;gap:10px}
.brand .dot{width:16px;height:16px;border-radius:50%;background:var(--ink)}
.brand .name{font-family:"Source Sans 3",sans-serif;font-weight:700;font-size:30px;color:var(--red);line-height:1}
.contact{position:absolute;left:618px;top:60px;display:flex;gap:8px;align-items:center;white-space:nowrap}
.contact .phone{font-size:18px;line-height:1;letter-spacing:.5px}
.contact .mail{font-size:9.5px;color:var(--red)}
.social{position:absolute;left:833px;top:61px;display:flex;gap:8px}
.social span{width:34px;height:34px;border-radius:50%;background:var(--red);border:2px solid #7a0a18}

.nav{position:absolute;top:120px;left:0;width:1200px;height:44px;background:linear-gradient(#d9283f,#a80d24 60%,#c8102e)}
.nav ul{list-style:none;display:flex;position:absolute;left:250px;height:44px}
.nav li{font-family:"Ubuntu",sans-serif;font-size:12px;color:var(--white);letter-spacing:.5px;padding:0 26px;line-height:44px;border-right:1px solid rgba(255,255,255,.25)}
.nav li:last-child{border:none}
.nav li.current{background:linear-gradient(#000,#2a2a2a);padding:0 30px}

.hero{position:absolute;top:164px;left:0;width:1200px;height:222px;background:linear-gradient(#fafafa,#f0f0f0 70%,#dcdcdc 71%,#f4f4f4);border-bottom:1px solid #ddd}

.intro{top:394px;height:62px;border-top:3px solid var(--ink);border-bottom:3px solid var(--ink);text-align:center;padding-top:10px}
.intro h1{font-weight:400;font-size:16.5px;color:var(--red)}
.intro p{font-size:14px}

.cols{top:484px;display:flex;gap:6px;left:255px}
.col{width:165px}
.col h2{font-weight:400;font-size:18px;color:var(--red);border-bottom:3px solid var(--ink);padding-left:35px;line-height:22px;white-space:nowrap}
.col h3{font-weight:700;font-size:11.5px;line-height:14px;margin:5px 0 10px}
.col p{font-size:9.5px;line-height:16.5px;height:106px}
.more{display:inline-block;width:75px;height:21px;background:var(--red);border:2px solid #6b0815;color:var(--white);font-family:"Ubuntu",sans-serif;font-size:9.5px;text-align:center;line-height:17px}
.col.list{margin-left:8px}
.col.list ul{list-style:none;text-align:center;font-size:12.5px;line-height:17.2px;margin-top:4px}

.testimonial{top:715px;height:85px;background:var(--bar);color:var(--white);text-align:center;padding:13px 18px}
.testimonial h2{font-weight:400;font-size:17px;margin-bottom:5px}
.testimonial p{font-size:10px;line-height:12px}

.support{top:812px}
.support .label{font-size:8.5px;color:#666;padding-left:8px}
.badges{display:flex;gap:18px;margin-top:6px;padding-left:8px}
.badges .wide{width:88px;height:36px;background:linear-gradient(90deg,#f3c6cf,#d9e7f5,#f7e3a8)}
.badges .square{width:34px;height:36px;background:#111}

.footer{top:887px;border-top:1px solid #ddd;padding-top:3px;display:flex;justify-content:space-between;font:7px Arial,sans-serif;color:var(--ink);padding-left:7px}
</style>
</head>
<body>
<header class="topbar">
  <div class="audience">CLIENT &nbsp;| &nbsp;<span class="active">JOB SEEKER</span></div>
  <div class="login">
    <div class="field">EMAIL</div>
    <div class="field">PASSWORD</div>
    <div class="btn">LOGIN</div>
    <div class="btn">SIGN UP</div>
  </div>
  <div class="login-notes" style="left:639px">Keep me logged in</div>
  <div class="login-notes" style="left:761px">Forgot your password?</div>
</header>

<div class="brand"><span class="dot"></span><span class="name">Lunvale Placements</span></div>

<div class="contact">
  <svg width="30" height="32" viewBox="0 0 30 32" aria-hidden="true">
    <rect x="2" y="12" width="26" height="18" fill="var(--red)"/>
    <path d="M2 12 L15 23 L28 12" fill="none" stroke="#fff" stroke-width="2"/>
    <path d="M4 9 q0-7 7-7 l2 4 -3 2 q1 3 3 4" fill="none" stroke="var(--ink)" stroke-width="2.5"/>
  </svg>
  <div><div class="phone">61-3-95550142</div><div class="mail">admin@lunvaleplacements.example</div></div>
</div>
<div class="social"><span></span><span></span><span></span></div>

<nav class="nav">
  <ul>
    <li class="current">Home</li>
    <li>Migration assistance</li>
    <li>Job seeker</li>
    <li>Useful links</li>
    <li>Support</li>
    <li>Contact us</li>
  </ul>
</nav>

<div class="hero" role="img" aria-label="Light grey world map with a row of red business people silhouettes and a speech bubble"></div>

<section class="wrap intro">
  <h1>We are Executive search and selection specialiats</h1>
  <p>We work exclcsively with our clints</p>
</section>

<section class="wrap cols">
  <article class="col">
    <h2>Who we are</h2>
    <h3>We have recruited for over 400 leading companies</h3>
    <p>This great online booking and appointment system offer is when avaible when you use SlotBook and PayLink.</p>
    <span class="more">Read more</span>
  </article>
  <article class="col">
    <h2>What we do</h2>
    <h3>We are a specialist recruiter to the health sector.</h3>
    <p>Exclusive offer to PayLink account holders. Offer covers all your ink and toner needs and includes delivery and 100% guarantee.</p>
    <span class="more">Read more</span>
  </article>
  <article class="col">
    <h2>Our Approach</h2>
    <h3>Make your business the best it can be</h3>
    <p>From step-by-step gudes to hints and tips, you'll find everything you need to help you grow your business and boost sales.</p>
    <span class="more">Read more</span>
  </article>
  <article class="col list">
    <h2>Job seeker from</h2>
    <ul>
      <li>United Kingdom</li><li>Middle East</li><li>Zimbabwe</li><li>Mayasia</li><li>Singapore</li><li>China</li><li>Philippines</li><li>New Zealand</li><li>South Africa</li><li>Botswana</li>
    </ul>
  </article>
</section>

<section class="wrap testimonial">
  <h2>Client's Testimonials</h2>
  <p>"thank you so much Marcus for finding our beautiful home. We were so fedup stressed the whole buying process, and your understanding and knowledge of the market really put our mind at ease and allowed us to buy with the confidence to know we were making the right decision. I finally have my weekends back."</p>
</section>

<section class="wrap support">
  <div class="label">We proudly support</div>
  <div class="badges"><span class="wide"></span><span class="square"></span></div>
</section>

<footer class="wrap footer">
  <span>Home &nbsp;•&nbsp; Who we are &nbsp;•&nbsp; Our Approach &nbsp;•&nbsp; What we do &nbsp;•&nbsp; Migration assistance &nbsp;•&nbsp; Job seeker &nbsp;•&nbsp; Useful links &nbsp;•&nbsp; Support &nbsp;•&nbsp; Contact us</span>
  <span>© Lunvale Partners 2008</span>
</footer>
</body>
</html>
```